Broschüre für externen Datenschutzpartner
Herzlichen Dank an KoLuxAr für die ausgezeichneten Arbeiten und das perfekte Ergebnis.
Zielgruppe
Korvento hat sich darauf spezialisiert, insbesondere kleine und mittelständische Unternehmen als externer Datenschutzpartner kontinuierlich zu betreuen und zu beraten. Durch neue Anforderungen – bereits heute durch die DS-GVO und zukünftig durch die EPVO – wird es zunehmend notwendig für Unternehmen, verstärkt externe Beratung mit entsprechendem Know-how in den Bereichen Datenschutz und IT-Sicherheit einzuholen. Denn der Schutz personenbezogener Daten sowie die geforderte Sicherheit haben durch die Gültigkeit der europaweit geltenden DS-GVO massiv an Bedeutung gewonnen. Dieser Trend wird durch die zunehmende Digitalisierung weiter zunehmen. Hier bieten wir ein breites Leistungsspektrum an.
Aufgabenstellung
Eine Broschüre als Vorlage ist beigefügt. (Brisalt-Info-NetzwerkAblauf.pdf) Es sollen ebenso alle relevanten Informationen auf die Seiten verteilt werden, ohne die Seiten zu überladen. Bei den Grafiken würden wir uns ähnliche Bilder (StockPhotos) wünschen. Die vorhandene CI der Korvento (www.korvento.de) soll dabei wieder zu erkennen sein.
Alle weiteren Informationen sind den beigefügten Dokumenten und der Website zu entnehmen. Die Broschüre soll das Präsentation dargestellt werden. zwischen 7-9 Seiten. Inhaltliche Fragen werden jederzeit beantwortet.

```html
<!DOCTYPE html>
<html lang="de">
<head>
<meta charset="utf-8">
<title>Korvento – Broschüre Datenschutz</title>
<link href="https://fonts.googleapis.com/css2?family=Montserrat:wght@300;400;500;600&display=swap" rel="stylesheet">
<style>
:root{
  --green:#3fb45a;
  --green-dark:#2f9a49;
  --green-pale:#e6f4e9;
  --grey-dark:#5e5e5e;
  --grey-mid:#8c8c8c;
  --grey-light:#e9e9e9;
  --paper:#ffffff;
  --text:#555555;
  --bg:#ececec;
}
*{box-sizing:border-box;margin:0;padding:0}
html,body{width:1200px;height:2880px;overflow:hidden}
body{background:var(--bg);font-family:"Montserrat",sans-serif;color:var(--text);position:relative}
.spread{position:absolute;left:100px;width:1000px;height:690px;display:flex;box-shadow:0 12px 30px rgba(0,0,0,.18)}
.spread-1{top:15px}.spread-2{top:735px}.spread-3{top:1455px}.spread-4{top:2175px}
.page{position:relative;width:500px;height:690px;background:var(--paper);overflow:hidden}
.page + .page{border-left:1px solid #dcdcdc}
.abs{position:absolute}
.body-text{font-size:8.5px;line-height:1.5;font-weight:400}
.h-light{font-weight:300;text-transform:uppercase;letter-spacing:.5px}
.white{color:#fff}
.brand-name{font-weight:500;letter-spacing:.5px}

/* cover */
.top-bar{position:absolute;left:0;top:0;width:100%;height:7px;background:var(--green)}
.pattern-area{position:absolute;left:0;top:7px;width:100%;height:373px;background:linear-gradient(180deg,#fafafa,#e4e4e4)}
.tagline{position:absolute;right:40px;top:40px;text-align:right;font-size:11px;line-height:1.5;text-transform:uppercase}
.tagline .accent{color:var(--green);font-weight:500}
.back-dark{position:absolute;left:0;bottom:0;width:100%;height:310px;background:var(--grey-dark)}
.back-name{left:60px;top:70px;font-size:34px;color:#fff}
.back-sub{left:62px;top:114px;font-size:8px;color:#ddd}
.contact{left:60px;top:160px;font-size:9px;line-height:1.7;color:#eee}
.contact-row{display:flex;gap:8px;align-items:flex-start}
.contact-row svg{flex:none;margin-top:3px}
.cover-name{left:40px;top:38px;font-size:46px;color:var(--grey-dark)}
.cover-sub{left:42px;top:96px;font-size:9px;color:var(--green);font-weight:500}
.photo-frame{left:190px;top:130px;width:290px;height:320px;border:10px solid var(--green);border-radius:40px;background:linear-gradient(135deg,#c9cdd2,#8b9096 60%,#5f6469)}
.front-dark{left:0;bottom:0;width:100%;height:300px;background:var(--grey-dark);clip-path:polygon(0 28%,100% 48%,100% 100%,0 100%)}
.cover-title{left:40px;bottom:60px;font-size:30px;line-height:1.2;color:#fff;font-weight:400}

/* spread 2 */
.concept-col{left:0;top:0;width:230px;height:690px;background:var(--green)}
.photo-top{left:150px;top:20px;width:350px;height:270px;background:linear-gradient(135deg,#dfe3e8,#aab0b7 55%,#7c8289)}
.concept-title{left:24px;top:300px;font-size:16px}
.concept-text{left:24px;top:332px;width:190px;color:#fff}
.concept-cta{left:24px;top:570px;width:190px;font-size:8.5px;font-weight:600;color:#fff}
.tasks-title{left:250px;top:310px;font-size:16px;color:var(--grey-dark)}
.tasks-text{left:250px;top:340px;width:220px}
.cta-tag{left:250px;top:588px;background:var(--green);color:#fff;font-size:9px;padding:4px 10px;text-transform:uppercase}
.phone-box{left:250px;top:610px;width:220px;height:40px;background:var(--grey-dark);color:#fff;font-size:15px;display:flex;align-items:center;gap:10px;padding-left:14px}
.section-title{font-size:15px;color:var(--grey-dark)}
.benefit-line{left:60px;top:95px;width:0;height:510px;border-left:2px dotted var(--green)}
.benefit{position:absolute;left:40px;width:430px;display:flex;gap:18px}
.icon-circle{flex:none;width:42px;height:42px;border-radius:50%;background:#fff;border:2px solid var(--green);display:flex;align-items:center;justify-content:center}
.benefit h3{font-size:10.5px;font-weight:500;text-transform:uppercase;color:var(--grey-dark);margin-bottom:4px}
.benefit .body-text{border-bottom:1px solid var(--green);padding-bottom:6px}
.bottom-bar{left:90px;top:630px;width:410px;height:46px;background:var(--green);color:#fff;font-size:10.5px;display:flex;align-items:center;padding-left:24px;text-transform:uppercase}

/* spread 3 */
.illustration{left:0;top:0;width:500px;height:690px;background:radial-gradient(circle at 50% 45%,#ffffff,#eef6f0 55%,#dcefe1)}
.ko-line{left:150px;top:360px;width:200px;text-align:center;color:var(--green);font-size:18px;font-weight:600;line-height:1.2;text-transform:uppercase}
.dark-band{left:0;top:0;width:500px;height:160px;background:linear-gradient(90deg,#6a6a6a,#4f4f4f)}
.band-title{left:0;top:64px;width:500px;text-align:center;font-size:13px;color:#fff;text-transform:uppercase;letter-spacing:.5px}
.pillar{position:absolute;top:122px;width:150px;text-align:center}
.pillar .icon-circle{margin:0 auto 8px;background:var(--green);border:3px solid #fff;width:50px;height:50px}
.pillar h3{font-size:10px;font-weight:500;text-transform:uppercase;color:var(--grey-dark);line-height:1.3;margin-bottom:6px}
.pillar .body-text{font-size:7.5px}
.pillar .accent{color:var(--green);font-weight:600}
.works-title{left:30px;top:390px}
.works-text{left:30px;top:420px;width:215px}
.works-text .accent{color:var(--green)}
.culture-box{left:265px;top:360px;width:235px;height:330px;background:var(--green);padding:28px 22px;color:#fff}
.culture-box h2{font-size:15px;font-weight:300;text-transform:uppercase;margin-bottom:14px}

/* spread 4 */
.pkg-band{left:0;top:0;width:1000px;height:240px;background:linear-gradient(90deg,var(--green) 35%,#2f8a45 55%,var(--green) 75%)}
.pkg-title{left:0;top:70px;width:1000px;text-align:center;font-size:12px;color:#fff;text-transform:uppercase;letter-spacing:.5px}
.pkg-card{position:absolute;top:170px;width:190px;text-align:center}
.price{width:70px;height:70px;border-radius:50%;background:#fff;border:4px solid var(--green);margin:0 auto -14px;position:relative;display:flex;align-items:center;justify-content:center;font-size:17px;color:var(--grey-dark)}
.pkg-head{background:var(--grey-mid);color:#fff;font-size:12px;padding:20px 0 8px;text-transform:uppercase;letter-spacing:.5px}
.pkg-card.featured .pkg-head{background:var(--green)}
.pkg-list{background:var(--grey-light);list-style:none;padding:8px 10px}
.pkg-list li{font-size:8px;text-transform:uppercase;padding:4px 0;border-bottom:1px solid #d2d2d2}
.pkg-list li:last-child{border-bottom:none}
.who-title{left:40px;top:485px;font-size:15px;color:var(--grey-dark)}
.who-item{position:absolute;left:40px;width:420px;display:flex;gap:12px;align-items:flex-start}
.num{flex:none;width:22px;height:22px;border-radius:50%;border:1.5px solid var(--green);font-size:10px;display:flex;align-items:center;justify-content:center;color:var(--grey-dark)}
.why-box{left:520px;top:530px;width:480px;height:160px;background:var(--green);padding:16px 26px;color:#fff}
.why-box h2{font-size:13px;font-weight:300;text-transform:uppercase;margin-bottom:8px}
.why-tag{left:760px;top:490px;font-size:8px;background:var(--grey-mid);color:#fff;padding:3px 8px;text-transform:uppercase}
.why-phone{left:760px;top:506px;width:200px;height:28px;background:var(--grey-dark);color:#fff;font-size:12px;display:flex;align-items:center;gap:8px;padding-left:10px}
</style>
</head>
<body>

<!-- Umschlag -->
<section class="spread spread-1">
  <div class="page back-cover">
    <div class="top-bar"></div>
    <div class="pattern-area" role="img" aria-label="Heller Hintergrund mit fließenden Binärziffern"></div>
    <p class="tagline">Schützen Sie, was wichtig ist.<br><span class="accent">Pragmatisch. Sicher. Kompetent!</span></p>
    <div class="back-dark">
      <div class="abs back-name brand-name">Korvento</div>
      <div class="abs back-sub">Professioneller Datenschutz für Unternehmen</div>
      <div class="abs contact">
        <div class="contact-row"><svg width="8" height="10" viewBox="0 0 8 10"><path d="M4 0a3.5 3.5 0 0 0-3.5 3.5C.5 6 4 10 4 10s3.5-4 3.5-6.5A3.5 3.5 0 0 0 4 0z" fill="#fff"/><circle cx="4" cy="3.5" r="1.3" fill="#5e5e5e"/></svg><span>Korvento GmbH &amp; Co. KG<br>Lindenallee 14<br>40210 Düsseldorf</span></div>
        <div class="contact-row" style="margin-top:10px"><svg width="9" height="9" viewBox="0 0 10 10"><path d="M2 0l2 2.5-1.2 1.3a6 6 0 0 0 3.4 3.4L7.5 6 10 8 8.5 10C4 10 0 6 0 1.5z" fill="#fff"/></svg><span>Tel.: 0211 4400 18 52 0</span></div>
        <div class="contact-row"><svg width="9" height="9" viewBox="0 0 10 8"><rect x=".5" y=".5" width="9" height="7" fill="none" stroke="#fff"/><path d="M.5.5l4.5 4 4.5-4" fill="none" stroke="#fff"/></svg><span>Mail: info@korvento.de</span></div>
        <div class="contact-row"><svg width="9" height="9" viewBox="0 0 10 10"><circle cx="5" cy="5" r="4.5" fill="#fff"/></svg><span>www.korvento.de</span></div>
      </div>
    </div>
  </div>
  <div class="page front-cover">
    <div class="top-bar"></div>
    <div class="abs cover-name brand-name">Korvento</div>
    <div class="abs cover-sub">Professioneller Datenschutz für Unternehmen</div>
    <div class="abs front-dark"></div>
    <div class="abs photo-frame" role="img" aria-label="Foto eines Ritters in Rüstung mit grünem Schild"></div>
    <h1 class="abs cover-title">IT-SICHERHEIT &amp;<br>DATENSCHUTZ</h1>
  </div>
</section>

<!-- Konzept & Vorteile -->
<section class="spread spread-2">
  <div class="page">
    <div class="abs concept-col"></div>
    <div class="abs photo-top" role="img" aria-label="Foto eines Ritters mit Schwert und grünem Schild"></div>
    <h2 class="abs concept-title h-light white">Unser Konzept</h2>
    <p class="abs concept-text body-text">Die Korvento GmbH &amp; Co. KG ist ein junges, dynamisches Beratungsunternehmen mit Sitz in Düsseldorf. Wir betreuen insbesondere kleine und mittelständische Unternehmen als externer Datenschutzpartner kontinuierlich und beraten sie.<br><br>Durch neue Anforderungen – bereits heute durch die DS-GVO und zukünftig durch die EPVO – wird externe Beratung mit Know-how in Datenschutz und IT-Sicherheit immer wichtiger.<br><br>Denn der Schutz personenbezogener Daten hat durch die europaweit geltende DS-GVO massiv an Bedeutung gewonnen. Dieser Trend wird durch die Digitalisierung weiter zunehmen.</p>
    <p class="abs concept-cta">HIER BIETEN WIR EIN BREITES LEISTUNGSSPEKTRUM AN.</p>
    <h2 class="abs tasks-title h-light">Unsere Aufgaben</h2>
    <p class="abs tasks-text body-text">Als Anbieter für externen Datenschutz und IT-Sicherheit verfügt Korvento über hochwertige inhaltliche sowie technische Expertise und bildet damit das Fundament für die Einhaltung der DS-GVO und der zukünftigen EPVO.<br><br>Zudem beraten wir Sie fortlaufend, um eine pragmatische Umsetzung der Anforderungen im Bereich Datenschutz zu gewährleisten.<br><br>Dazu zählen auch <strong>notwendige technische und organisatorische Maßnahmen.</strong><br><br>Als externe Datenschutzbeauftragte bringen wir die nötige Expertise mit, um Ihr Unternehmen zu beraten.</p>
    <div class="abs cta-tag">Worauf warten Sie?</div>
    <div class="abs phone-box"><svg width="14" height="14" viewBox="0 0 10 10"><path d="M2 0l2 2.5-1.2 1.3a6 6 0 0 0 3.4 3.4L7.5 6 10 8 8.5 10C4 10 0 6 0 1.5z" fill="#fff"/></svg>0211 4400 18 52 0</div>
  </div>
  <div class="page">
    <h2 class="abs section-title h-light" style="left:60px;top:40px">Ihre Vorteile</h2>
    <div class="abs benefit-line"></div>
    <div class="benefit" style="top:80px"><div class="icon-circle"><svg width="18" height="18" viewBox="0 0 20 20"><circle cx="8" cy="8" r="5.5" fill="none" stroke="#3fb45a" stroke-width="2"/><path d="M12 12l6 6" stroke="#3fb45a" stroke-width="2.5"/></svg></div><div><h3>Transparenz</h3><p class="body-text">Durch unsere individuellen Leistungspakete bekommen Sie den passenden Schutz ohne versteckte Extrakosten – ein transparentes und faires Angebot.</p></div></div>
    <div class="benefit" style="top:170px"><div class="icon-circle"><svg width="18" height="18" viewBox="0 0 20 20"><circle cx="10" cy="6" r="4" fill="#3fb45a"/><path d="M2 19a8 7 0 0 1 16 0z" fill="#3fb45a"/></svg></div><div><h3>Fokus</h3><p class="body-text">Fokus DS-GVO und e-Privacy: Gemeinsam überwinden wir die Hürden der neuen Datenschutzgesetze und konzentrieren uns zielgerichtet auf Ihr Unternehmen.</p></div></div>
    <div class="benefit" style="top:260px"><div class="icon-circle"><svg width="20" height="14" viewBox="0 0 20 14"><path d="M1 7l5-5 4 3 4-3 5 5-6 6-3-3-3 3z" fill="#3fb45a"/></svg></div><div><h3>Partnerschaft</h3><p class="body-text">Die Formel für eine optimale Kundenbeziehung ist der Erfolg, der sich aus Vertrauen und Problemverständnis zusammensetzt. Unsere Betreuung steht Ihnen jederzeit zur Verfügung.</p></div></div>
    <div class="benefit" style="top:350px"><div class="icon-circle"><svg width="16" height="20" viewBox="0 0 16 20"><circle cx="8" cy="7" r="6" fill="none" stroke="#3fb45a" stroke-width="2"/><path d="M4 12l-1 7 5-3 5 3-1-7" fill="#3fb45a"/></svg></div><div><h3>Kompetenz</h3><p class="body-text">Datenschutz ist ein sehr umfassendes Thema und bereitet noch vielen Unternehmen Schwierigkeiten. Wir gehen das Thema strukturiert und mit Fachexpertise an.</p></div></div>
    <div class="benefit" style="top:440px"><div class="icon-circle"><svg width="18" height="18" viewBox="0 0 20 20"><path d="M16 6a7 7 0 1 0 1 6" fill="none" stroke="#3fb45a" stroke-width="2.2"/><path d="M17 1v6h-6" fill="none" stroke="#3fb45a" stroke-width="2.2"/></svg></div><div><h3>Kontinuierliche Betreuung</h3><p class="body-text">Unsere Handlungsempfehlungen und alle zukünftigen Maßnahmen werden von uns erfolgreich umgesetzt. Eine kontinuierliche Betreuung sehen wir als selbstverständlich an.</p></div></div>
    <div class="benefit" style="top:530px"><div class="icon-circle"><svg width="20" height="16" viewBox="0 0 20 16"><rect x="2" y="1" width="16" height="10" fill="none" stroke="#3fb45a" stroke-width="2"/><path d="M0 14h20" stroke="#3fb45a" stroke-width="2.5"/></svg></div><div><h3>Technologie</h3><p class="body-text">Dank unserer Webplattform werden Ihnen zeit- und materialsparende Prozesse geboten. Durch unsere KorSafe Plattform (KSP) erkennen wir Probleme schnell und handeln ohne Umwege.</p></div></div>
    <div class="abs bottom-bar">Entscheiden Sie sich für den richtigen Service.</div>
  </div>
</section>

<!-- Ablauf & Kultur -->
<section class="spread spread-3">
  <div class="page">
    <div class="abs illustration" role="img" aria-label="Gezeichneter Ablaufkreis mit Ritter, grünen Pfeilen, Checkliste, Handschlag, Puzzle und Laptop mit Schritten der Zusammenarbeit"></div>
    <p class="abs ko-line">Kein KO durch<br>die DS-GVO!</p>
  </div>
  <div class="page">
    <div class="abs dark-band" role="img" aria-label="Dunkles Foto eines Ritters mit grünem Schild"></div>
    <p class="abs band-title">Pragmatisch. Sicher. Kompetent!</p>
    <div class="pillar" style="left:25px"><div class="icon-circle"><svg width="18" height="22" viewBox="0 0 18 22"><path d="M9 1a7 7 0 0 0-4 12.7V16h8v-2.3A7 7 0 0 0 9 1z" fill="#fff"/><rect x="5" y="18" width="8" height="3" fill="#fff"/></svg></div><h3>Warum<br>Korvento?</h3><p class="body-text">Wir rüsten Sie gegen Bedrohungen durch IT- und Cyberkriminalität sowie Datenklau und bieten die perfekte Betreuung, ganz gleich ob DS-GVO oder EPVO.</p></div>
    <div class="pillar" style="left:175px"><div class="icon-circle"><svg width="22" height="22" viewBox="0 0 22 22"><circle cx="11" cy="11" r="6" fill="none" stroke="#fff" stroke-width="4" stroke-dasharray="3 2"/><circle cx="11" cy="11" r="2.5" fill="#fff"/></svg></div><h3>Unsere<br>Maßnahmen</h3><p class="body-text">Passende Leistungspakete für jedes Unternehmen helfen Ihnen, die neue DS-GVO in Ihrem Unternehmen problemlos zu integrieren und optimal umzusetzen.</p></div>
    <div class="pillar" style="left:325px"><div class="icon-circle"><svg width="22" height="22" viewBox="0 0 22 22"><circle cx="9" cy="9" r="6.5" fill="none" stroke="#fff" stroke-width="2.2"/><path d="M6 9l2 2 4-4M14 14l6 6" fill="none" stroke="#fff" stroke-width="2.2"/></svg></div><h3>Unsere<br>Kontrolle</h3><p class="body-text"><span class="accent">VERTRAUEN IST GUT – KONTROLLE IST BESSER!</span> Durch externe Datenschutzbeauftragte gewinnen Sie das Vertrauen Ihrer Kunden und vermeiden unnötige Abmahnungen.</p></div>
    <h2 class="abs section-title h-light works-title">Unsere Arbeiten</h2>
    <p class="abs body-text works-text">Unsere Datenschutzexperten vereinbaren zunächst einen Termin mit Ihnen und kommen persönlich in Ihr Unternehmen. Bei diesem detaillierten Datenschutz-Audit stellen wir den notwendigen Handlungsbedarf fest und begleiten Sie kompetent und pragmatisch bei den erforderlichen Maßnahmen, sowohl intern als auch extern.<br><br>Durch unsere Kundenplattform bieten wir Ihnen darüber hinaus zeit- und materialsparende Prozesse an. Einen ersten Check Ihrer Website werden wir zukünftig durch den Einsatz unserer geplanten <span class="accent">KorSafe Plattform (KSP)</span> vornehmen können. Somit kommt es nicht zu unnötigen Abmahnungen.</p>
    <div class="abs culture-box">
      <h2>Unsere Kultur</h2>
      <p class="body-text">Wir sind stets positiv eingestellt, gehen respektvoll miteinander um und arbeiten pragmatisch und hoch professionell. Teamarbeit und persönliche Wertschätzung stehen bei uns an erster Stelle. Dazu zählt persönliche Leistung genauso wie Eigenständigkeit.<br><br><strong>Die Formel für eine optimale Kundenbeziehung</strong> ist der Erfolg, der sich aus Vertrauen und Problemverständnis zusammensetzt – durch unsere Betreuung stehen Ihnen unsere gesamte Kompetenz und unser Expertenwissen für maximalen Erfolg zur Verfügung.</p>
    </div>
  </div>
</section>

<!-- Leistungspakete -->
<section class="spread spread-4">
  <div class="page"></div>
  <div class="page"></div>
  <div class="abs pkg-band" role="img" aria-label="Grün getöntes Foto eines Ritters mit Schild"></div>
  <p class="abs pkg-title">Das für Sie passende Leistungspaket</p>
  <div class="pkg-card" style="left:40px"><div class="price">150€</div><div class="pkg-head">Leistung S</div><ul class="pkg-list"><li>Einzelhandel</li><li>Gastronomie</li><li>KFZ Betriebe</li><li>Handwerksbetriebe</li><li>Baugewerbe</li></ul></div>
  <div class="pkg-card" style="left:280px"><div class="price">250€</div><div class="pkg-head">Leistung M</div><ul class="pkg-list"><li>Agenturen &amp; Makler</li><li>Werbebranche</li><li>Ärzte und Apotheker</li><li>Online Shops/E-Commerce</li><li>Transport &amp; Logistik</li></ul></div>
  <div class="pkg-card" style="left:530px"><div class="price">350€</div><div class="pkg-head">Leistung L</div><ul class="pkg-list"><li>Medizin und Gesundheitswesen</li><li>Steuerberater</li><li>Medienunternehmen</li><li>Marketing</li></ul></div>
  <div class="pkg-card featured" style="left:770px"><div class="price">500€</div><div class="pkg-head">Leistung XL</div><ul class="pkg-list"><li>KMU's mit über 100 MA</li><li>Personal-Service</li><li>Finanzdienstleister</li><li>Produzierendes Gewerbe</li><li>Industrie</li></ul></div>
  <h2 class="abs who-title h-light">Wer braucht Datenschutz?</h2>
  <div class="who-item" style="top:525px"><span class="num">1</span><p class="body-text">Privatrechtliche Organisationen und Firmen, aber auch Personen, die personenbezogene Daten verarbeiten (z.B. Selbstständige, Produktions-, Handels- und Dienstleistungsunternehmen).</p></div>
  <div class="who-item" style="top:575px"><span class="num">2</span><p class="body-text">Sonstige privatrechtliche Organisationen, deren Geschäftszweck die Verarbeitung personenbezogener Daten für Dritte ist (z.B. Service-Rechenzentren oder Forschungseinrichtungen).</p></div>
  <div class="who-item" style="top:625px"><span class="num">3</span><p class="body-text">Öffentliche Stellen des Bundes und der Länder (z.B. Bundesbehörden und Kommunalverwaltungen).</p></div>
  <div class="abs why-tag">Worauf warten Sie?</div>
  <div class="abs why-phone"><svg width="11" height="11" viewBox="0 0 10 10"><path d="M2 0l2 2.5-1.2 1.3a6 6 0 0 0 3.4 3.4L7.5 6 10 8 8.5 10C4 10 0 6 0 1.5z" fill="#fff"/></svg>0211 4400 18 52 0</div>
  <div class="abs why-box">
    <h2>Warum Korvento?</h2>
    <p class="body-text">Wir gewährleisten eine fehlerfreie Implementierung und Einhaltung eines ausreichenden Datenschutzes einschließlich der notwendigen technischen Voraussetzung. Zudem betreuen wir Sie kontinuierlich, sodass alle Abläufe den gesetzlichen Anforderungen gerecht werden. Unsere individualisierten Leistungspakete bieten die optimale Betreuung für jede Unternehmensgröße. Sämtliche Leistungen sind auch individuell buchbar – ein transparentes und faires Angebot.</p>
  </div>
</section>

</body>
</html>
```